I need to refresh my meeting minutes pages (2 of them)

I have 2 pages that need to be modernized with a new look and feel. I have attached the 2 pages that need the refresh. I am okay with one page submissions as long as the winner is willing to add the second page before payment :-) Any questions please let me know. The logo on the page is not ours but a sample of what client may give us.

```html
<!DOCTYPE html>
<html lang="en">
<head>
<meta charset="utf-8">
<title>Agenda Item Details</title>
<link href="https://fonts.googleapis.com/css2?family=Bricolage+Grotesque:wght@400;500;600;700&display=swap" rel="stylesheet">
<style>
:root{
  --ink:#15171c;
  --ink-soft:#3a3d44;
  --muted:#6b6f78;
  --line:#e6e7ea;
  --rail:#1b1e24;
  --rail-text:#c9ccd2;
  --accent:#d7282f;
  --accent-tint:#fde9ea;
  --chip:#f3f4f5;
  --page:#f7f7f8;
  --link:#1a7ee0;
  --white:#ffffff;
}
*{box-sizing:border-box;margin:0;padding:0}
html,body{width:1200px;height:750px;overflow:hidden}
body{font-family:"Bricolage Grotesque",sans-serif;color:var(--ink);background:var(--page);position:relative}
svg{display:block}
.topbar{position:absolute;left:0;top:0;width:1200px;height:53px;background:var(--white);display:flex;align-items:center;justify-content:space-between;padding:0 20px;box-shadow:0 1px 3px rgba(0,0,0,.05);z-index:2}
.brand{font-size:17px;font-weight:700;letter-spacing:-.2px}
.powered{font-size:10.5px;color:var(--muted);line-height:1.5}
.powered u{text-underline-offset:2px}
.rail{position:absolute;left:0;top:53px;width:67px;height:697px;background:var(--rail)}
.rail-item{height:60px;display:flex;flex-direction:column;align-items:center;justify-content:center;gap:5px;color:var(--rail-text);font-size:9.5px}
.rail-item.active{background:var(--accent);color:var(--white)}
.agenda-list{position:absolute;left:67px;top:53px;width:333px;height:697px;background:var(--white);border-right:1px solid var(--line);overflow:hidden}
.search-wrap{height:64px;padding:14px 20px 0;border-bottom:1px solid var(--line)}
.search{height:36px;border:1px solid #d9dbdf;border-radius:4px;display:flex;align-items:center;gap:12px;padding:0 12px;font-size:12.5px;color:#a3a6ad}
.scrollbar{position:absolute;left:326px;top:66px;width:3px;height:200px;border-radius:2px;background:#cfd1d5}
.section{padding:13px 20px 13px;border-bottom:1px solid var(--line)}
.section-title{font-size:10.5px;font-weight:700;letter-spacing:.1px;height:14px;line-height:14px;margin-bottom:13px}
.item{position:relative;min-height:35px;background:var(--chip);border-radius:4px;padding:8px 12px 8px 40px;font-size:12.5px;line-height:15px;display:flex;align-items:center;margin-bottom:2px;color:var(--ink-soft)}
.item:last-child{margin-bottom:0}
.item svg{position:absolute;left:13px;top:50%;transform:translateY(-50%)}
.item.active{background:var(--accent-tint);color:var(--accent);font-weight:700}
.main{position:absolute;left:400px;top:53px;width:800px;height:697px;padding:14px 33px 0}
.toolbar{display:flex;align-items:center;height:37px}
.btn-group{display:flex;border:1px solid #d6d8dc;border-radius:4px;background:var(--white)}
.btn{width:39px;height:37px;display:flex;align-items:center;justify-content:center;background:var(--white);border:1px solid #d6d8dc;border-radius:4px}
.btn-group .btn{border:none;border-radius:0}
.btn-group .btn+.btn{border-left:1px solid #d6d8dc}
.print{margin-left:21px}
.share{margin-left:auto;width:40px}
.page-title{font-size:22px;font-weight:700;letter-spacing:-.3px;margin-top:22px;height:30px;line-height:30px}
.details{margin-top:15px;background:var(--white);border-radius:7px;padding:0 20px 20px;box-shadow:0 1px 2px rgba(0,0,0,.03)}
.row{display:flex;align-items:center;height:56px;border-bottom:1px solid var(--line);font-size:12.5px}
.row dt{width:214px;font-weight:600}
.row dd{color:var(--ink-soft)}
.attachment{margin-top:20px;height:35px;background:var(--chip);border-radius:4px;display:flex;align-items:center;padding:0 14px 0 13px;gap:12px;font-size:12.5px}
.attachment a{color:var(--link);font-weight:600;text-decoration:none}
.attachment .size{margin-left:auto;color:var(--muted)}
</style>
</head>
<body>
<header class="topbar">
  <div class="brand">ClientName</div>
  <div class="powered">Powered by:<br><u>AgendaWorks</u>® A Meridian Brand, © 2002–2025</div>
</header>

<nav class="rail">
  <div class="rail-item">
    <svg width="17" height="17" viewBox="0 0 24 24" fill="none" stroke="currentColor" stroke-width="1.6"><circle cx="12" cy="12" r="10"/><path d="M12 6.5l1.6 3.3 3.6.5-2.6 2.5.6 3.6-3.2-1.7-3.2 1.7.6-3.6-2.6-2.5 3.6-.5z"/></svg>
    <span>Featured</span>
  </div>
  <div class="rail-item">
    <svg width="17" height="17" viewBox="0 0 24 24" fill="none" stroke="currentColor" stroke-width="1.6"><circle cx="12" cy="5" r="2.5"/><rect x="6" y="9" width="12" height="6" rx="1"/><circle cx="5" cy="17" r="2"/><circle cx="19" cy="17" r="2"/><path d="M2 22c0-2 1.5-3 3-3s3 1 3 3M16 22c0-2 1.5-3 3-3s3 1 3 3"/></svg>
    <span>Meetings</span>
  </div>
  <div class="rail-item active">
    <svg width="17" height="17" viewBox="0 0 24 24" fill="none" stroke="currentColor" stroke-width="1.6"><rect x="3" y="4" width="17" height="16" rx="2"/><path d="M3 9h17M8 2v4M15 2v4"/><circle cx="17" cy="17" r="4" fill="var(--accent)"/><path d="M17 15.5V17l1 1"/></svg>
    <span>Agenda</span>
  </div>
  <div class="rail-item">
    <svg width="17" height="17" viewBox="0 0 24 24" fill="none" stroke="currentColor" stroke-width="1.6"><rect x="4" y="3" width="16" height="18" rx="3"/><circle cx="12" cy="12" r="3.5"/><path d="M8 6h8"/></svg>
    <span>Policies</span>
  </div>
</nav>

<aside class="agenda-list">
  <div class="search-wrap">
    <div class="search">
      <svg width="15" height="15" viewBox="0 0 24 24" fill="none" stroke="#2a2d33" stroke-width="2"><circle cx="10.5" cy="10.5" r="6.5"/><path d="M15.5 15.5L21 21"/></svg>
      <span>Search Agenda</span>
    </div>
  </div>
  <div class="scrollbar"></div>

  <section class="section">
    <h3 class="section-title">*R* WELCOME</h3>
    <div class="item">Wireless Access For Guests</div>
  </section>
  <section class="section">
    <h3 class="section-title">*R* CALL TO ORDER</h3>
    <div class="item">Pledge Of Allegiance</div>
    <div class="item">Roll Call</div>
  </section>
  <section class="section">
    <h3 class="section-title">RIVERTON PROUD</h3>
    <div class="item"><svg width="14" height="14" viewBox="0 0 24 24" fill="none" stroke="currentColor" stroke-width="1.8"><path d="M6 2h8l5 5v15H6z"/><path d="M9 12h7M9 16h7M9 8h3"/></svg>Westbrook Hockey Coach</div>
    <div class="item" style="min-height:50px"><svg width="14" height="14" viewBox="0 0 24 24" fill="none" stroke="currentColor" stroke-width="1.8"><path d="M6 2h8l5 5v15H6z"/><path d="M9 12h7M9 16h7M9 8h3"/></svg>Teaching Professions - Future Educators<br>State Competition</div>
  </section>
  <section class="section">
    <h3 class="section-title">*R* INFORMATION TO THE BOARD</h3>
    <div class="item">Superintendent - ACES/PAGE/First Step</div>
    <div class="item"><svg width="14" height="14" viewBox="0 0 24 24" fill="none" stroke="currentColor" stroke-width="1.8"><path d="M6 2h8l5 5v15H6z"/><path d="M9 12h7M9 16h7M9 8h3"/></svg>ACES</div>
    <div class="item active"><svg width="14" height="14" viewBox="0 0 24 24" fill="none" stroke="currentColor" stroke-width="1.8"><path d="M6 2h8l5 5v15H6z"/><path d="M9 12h7M9 16h7M9 8h3"/></svg>PAGE</div>
    <div class="item"><svg width="14" height="14" viewBox="0 0 24 24" fill="none" stroke="currentColor" stroke-width="1.8"><path d="M6 2h8l5 5v15H6z"/><path d="M9 12h7M9 16h7M9 8h3"/></svg>First Step</div>
  </section>
  <section class="section">
    <h3 class="section-title">*R* COMMUNICATION(S)</h3>
    <div class="item">Board Members -</div>
    <div class="item">&nbsp;</div>
  </section>
</aside>

<main class="main">
  <div class="toolbar">
    <div class="btn-group">
      <div class="btn"><svg width="12" height="12" viewBox="0 0 24 24" fill="none" stroke="#15171c" stroke-width="2.4"><path d="M15 5l-7 7 7 7"/></svg></div>
      <div class="btn"><svg width="12" height="12" viewBox="0 0 24 24" fill="none" stroke="#15171c" stroke-width="2.4"><path d="M9 5l7 7-7 7"/></svg></div>
    </div>
    <div class="btn print"><svg width="15" height="15" viewBox="0 0 24 24" fill="none" stroke="#15171c" stroke-width="2"><path d="M7 8V3h10v5"/><rect x="3" y="8" width="18" height="9" rx="2"/><rect x="7" y="14" width="10" height="7"/></svg></div>
    <div class="btn share"><svg width="15" height="15" viewBox="0 0 24 24" fill="none" stroke="#15171c" stroke-width="2"><circle cx="18" cy="5" r="3"/><circle cx="6" cy="12" r="3"/><circle cx="18" cy="19" r="3"/><path d="M8.6 10.6l6.8-4M8.6 13.4l6.8 4"/></svg></div>
  </div>

  <h1 class="page-title">Agenda Item Details</h1>

  <div class="details">
    <dl>
      <div class="row"><dt>Meeting</dt><dd>April 10, 2025 - Regular Meeting Agenda</dd></div>
      <div class="row"><dt>Category</dt><dd>*R* INFORMATION TO THE BOARD</dd></div>
      <div class="row"><dt>Subject</dt><dd>PAGE</dd></div>
      <div class="row"><dt>Type</dt><dd>-</dd></div>
    </dl>
    <div class="attachment">
      <svg width="14" height="14" viewBox="0 0 24 24" fill="none" stroke="#6b6f78" stroke-width="1.8"><path d="M6 2h8l5 5v15H6z"/><path d="M9 12h7M9 16h7M9 8h3"/></svg>
      <a href="#">2025-04-10 - Riverton Proud - PAGE (1).pdf</a>
      <span class="size">40 KB</span>
    </div>
  </div>
</main>
</body>
</html>
```